Custom Soapstone Shower Floor Brochure

Brody, after some thought and a very close look at your services. I have decided to enter into a design agreement with ArtLoomly. The following task is what I need help with:

1) While using our logo develop a captivating, informative and attractive double sided brochure (that can be printed on standard high gloss paper (8 1/2" x 11") that will draw interest and attention to our product shower floors. Information at northridgeslabworks.com. I would like any one picking up the brochure (at a trade show for example) to want to ask questions regarding the product we are selling "shower floors". There should be text and photos. (I have attached a few samples)

I am leaving everything up to your creative team, scour the internet for information, re-write my text. Essentially come up with something that high end hotels and commercial clients will be drawn to.

Thanking you in advance,

Hal

Target Market(s)

Hotels, commercial condominium clients, non residential.

Industry/Entity Type

Commercial

Font styles to use
Other font styles liked:
• The logo is in Veranda font however we are no married to it.

Colors

Designer to choose colors to be used in the design.

Requirements
Must have
• Informative text and pictures describing our product in a way that it will want to make people ask more questions.
Nice to have
• Pictures showcasing the shower floors, I can send more pictures if allowed.
Should not have
• Extremely bright colors.

```html
<!DOCTYPE html>
<html lang="en">
<head>
<meta charset="utf-8">
<title>Northridge Slabworks – Shower Floor Brochure</title>
<link href="https://fonts.googleapis.com/css2?family=Oswald:wght@400;500&family=Open+Sans:wght@400;600&family=Montserrat:wght@300;400&display=swap" rel="stylesheet">
<style>
  :root{
    --board:#dde1e1;
    --ink:#2b2f31;
    --charcoal:#202426;
    --paper:#ffffff;
    --slate:#4a5052;
    --muted:#d9dcdc;
    --photo-bath-a:#8e959a;
    --photo-bath-b:#3f4447;
    --photo-stone-a:#a9bfc8;
    --photo-stone-b:#5e7882;
  }
  *{margin:0;padding:0;box-sizing:border-box}
  html,body{width:1200px;height:1200px;overflow:hidden;background:var(--board)}
  body{position:relative;font-family:"Open Sans",sans-serif;color:var(--ink)}
  .side-label{position:absolute;left:0;width:1200px;text-align:center;font-family:"Oswald",sans-serif;font-weight:500;font-size:39px;color:var(--ink);line-height:1}
  .side-label--front{top:40px}
  .side-label--back{top:620px}

  .sheet{position:absolute;overflow:hidden}
  .sheet--front{left:294px;top:101px;width:612px;height:473px;background:var(--paper)}
  .sheet--back{left:288px;top:680px;width:624px;height:482px;background:var(--paper)}
  .abs{position:absolute}
  .photo{position:absolute}

  .heading{font-family:"Oswald",sans-serif;font-weight:400;color:var(--ink);line-height:1.2}
  .heading--section{font-size:13.5px;border-bottom:1px solid var(--ink);padding-bottom:1px;display:inline-block}
  .body-copy{font-size:6.6px;line-height:1.38;text-align:justify;color:#1c1c1c}
  .body-copy p+p{margin-top:6px}

  /* front left page */
  .about-heading{left:142px;top:28px}
  .about-copy{left:142px;top:56px;width:136px}
  .surface-heading{left:142px;top:165px;font-size:13px;width:140px}
  .surface-copy{left:142px;top:210px;width:136px;font-size:6.2px}
  .contact-band{left:0;top:363px;width:306px;height:100px;background:var(--charcoal);color:#fff;text-align:center}
  .contact-band .brand-name{margin-top:40px;font-size:10.5px;color:#fff}
  .contact-band .brand-sub{font-size:4.5px;margin-top:3px;color:#ccc}
  .contact-band .contact-lines{font-size:7.2px;line-height:1.55;margin-top:11px;letter-spacing:.1px}
  .brand-mark{display:block;margin:0 auto;border-radius:50%;background:var(--slate)}

  /* front cover */
  .cover{left:306px;top:0;width:306px;height:473px}
  .cover-brand{position:absolute;left:0;top:22px;width:306px;text-align:center}
  .cover-brand .brand-name{font-size:16px;color:var(--ink);margin-top:8px}
  .cover-brand .brand-sub{font-size:7.5px;color:var(--slate);margin-top:3px}
  .cover-rule{left:0;top:106px;width:306px;height:6px;background:var(--slate)}
  .cover-footer{left:0;top:338px;width:306px;height:135px;background:var(--charcoal);color:#fff;text-align:center;font-family:"Montserrat",sans-serif}
  .cover-footer .kicker{font-weight:300;font-size:22px;letter-spacing:1px;margin-top:18px}
  .cover-footer .title{font-weight:400;font-size:35px;letter-spacing:1.5px;line-height:1;margin-top:2px}
  .cover-footer .tagline{font-weight:300;font-size:12px;letter-spacing:.4px;margin-top:6px}
  .cover-footer .url{font-weight:300;font-size:8px;letter-spacing:2.2px;margin-top:14px}

  /* back left page */
  .back-left{left:0;top:0;width:311px;height:482px;background:var(--charcoal);color:#fff}
  .luxury-heading{left:18px;top:17px;color:#fff;font-size:13.5px;border-bottom:1px solid #fff;padding-bottom:2px;width:250px}
  .luxury-copy{left:118px;top:50px;width:164px;color:#e8e8e8;font-size:6.4px;line-height:1.45}
  .framed{position:absolute;border:2px solid #fff}
  .products-label{left:170px;top:311px;color:#fff;font-size:17.5px}

  /* back right page */
  .back-right{left:311px;top:0;width:313px;height:482px;background:var(--paper)}
  .floors-heading{left:14px;top:250px;font-size:19px;font-weight:500}
  .importance-heading{left:14px;top:279px;font-size:13px}
  .importance-copy{left:14px;top:309px;width:284px;font-size:6.5px;text-align:left}
  .products-heading{left:14px;top:344px;font-size:13px}
  .products-copy{left:14px;top:371px;width:284px;font-size:6.5px;text-align:left}
  .back-brand{left:0;top:430px;width:313px;text-align:center}
  .back-brand .brand-name{font-size:10.5px;color:var(--ink);margin-top:4px}
  .back-brand .brand-sub{font-size:4.5px;color:var(--ink);margin-top:2px}
</style>
</head>
<body>

<div class="side-label side-label--front">Front</div>

<section class="sheet sheet--front">
  <div class="photo" style="left:15px;top:50px;width:117px;height:98px;background:linear-gradient(160deg,#c9c3bd,#eceef0 55%,#6a6f75)" role="img" aria-label="Bathroom with white vanity cabinet and stone countertop"></div>
  <h2 class="abs heading heading--section about-heading">About Us</h2>
  <div class="abs body-copy about-copy">
    <p>Northridge Slabworks is a producer of countertops, shower bases / basins and architectural stone.</p>
    <p>Northridge Slabworks is the darling of soapstone varieties for it's unique beauty, character and durability. We are a LEED designated product that is green from quarrying to installation.</p>
  </div>

  <h2 class="abs heading heading--section surface-heading">Northridge Slabworks Is The Best Natural Surface</h2>
  <div class="photo" style="left:15px;top:210px;width:117px;height:98px;background:linear-gradient(120deg,#a9b3a4,#dfe3df 50%,#2f3436)" role="img" aria-label="Locker room with stone shower floor"></div>
  <div class="abs body-copy surface-copy">
    <p>It is the only non-porous stone on earth. Pores cannot be completely sealed, no matter the sealer, thus exposing other non-solid surfaces to bacteria and potential stains caused by everyday use.</p>
    <p>Secondly, due to its neutral-mineral content, soapstone is impervious to chemicals and therefore can be cleaned using even the strongest of household cleaning products; applying chemicals to other natural stone surfaces will typically damage them.</p>
  </div>

  <div class="abs contact-band">
    <div class="brand-name">Northridge Slabworks</div>
    <div class="brand-sub">Stainless Stone</div>
    <div class="contact-lines">EMAILS WILL BE RETURNED WITHIN 24 HOURS<br>CONTACT US AT 1.555.240.0187</div>
  </div>

  <div class="abs cover">
    <div class="cover-brand">
      <span class="brand-mark" style="width:18px;height:18px"></span>
      <div class="brand-name">Northridge Slabworks</div>
      <div class="brand-sub">Stainless Stone</div>
    </div>
    <div class="abs cover-rule"></div>
    <div class="photo" style="left:0;top:112px;width:306px;height:226px;background:linear-gradient(135deg,var(--photo-bath-a),#d8dadb 45%,var(--photo-bath-b))" role="img" aria-label="Hotel bathroom with twin vessel sinks, tall mirrors and stone wall"></div>
    <div class="abs cover-footer">
      <div class="kicker">THE ARCHITECTS</div>
      <div class="title">CHOICE</div>
      <div class="tagline">Elegant, Leading Edge And Affordable</div>
      <div class="url">northridgeslabworks.com</div>
    </div>
  </div>
</section>

<div class="side-label side-label--back">Back</div>

<section class="sheet sheet--back">
  <div class="abs back-left">
    <h2 class="abs heading luxury-heading">Luxury And Durability Meet The Shower Floor</h2>
    <div class="photo" style="left:16px;top:50px;width:94px;height:62px;background:linear-gradient(150deg,#d8dde2,#6f8596)" role="img" aria-label="Bathroom with soapstone floor and pedestal sink"></div>
    <div class="photo" style="left:16px;top:120px;width:94px;height:62px;background:linear-gradient(150deg,#c5cbd0,#5d7180)" role="img" aria-label="Walk-in shower with soapstone walls"></div>
    <div class="photo" style="left:16px;top:190px;width:94px;height:64px;background:linear-gradient(150deg,#9ea7ad,#465159)" role="img" aria-label="Corner shower with soapstone floor"></div>
    <div class="abs body-copy luxury-copy">
      Imagine a solid stone shower floor that requires less attention than a plastic shower pan or tiled shower floor.<br>
      Northridge Slabworks' patented shower floor makes this possible.<br>
      Northridge Slabworks within a shower floor means little upkeep and a host of other benefits. Density of our Soapstone in combination high saturation of talc make for a non porous floor. Soap scum and other residues sit on the surface, requiring a light scrub every 2 weeks.<br>
      It is the only non-porous stone on earth. Pores cannot be completely sealed, no matter the sealer, thus exposing other non-solid surfaces to bacteria and potential stains caused by everyday use.<br>
      Secondly, due to its neutral-mineral content, soapstone is impervious to chemicals and therefore can be cleaned using even the strongest of household cleaning products; applying chemicals to other natural stone surfaces will typically damage them.
    </div>
    <div class="framed" style="left:22px;top:278px;width:141px;height:98px;background:linear-gradient(140deg,#e3e4e0,#7d8b93 60%,#3c474e)" role="img" aria-label="Bathroom with soapstone shower floor and toilet"></div>
    <h2 class="abs heading products-label">Our Products</h2>
    <div class="framed" style="left:144px;top:362px;width:139px;height:97px;background:linear-gradient(160deg,#c9d0cf,#77858b)" role="img" aria-label="Close view of soapstone shower floor behind glass"></div>
  </div>

  <div class="abs back-right">
    <div class="photo" style="left:0;top:0;width:313px;height:246px;background:linear-gradient(135deg,var(--photo-stone-a),#8aa3ad 50%,var(--photo-stone-b))" role="img" aria-label="Soapstone shower wall with rain shower head and purple orchid"></div>
    <h2 class="abs heading floors-heading">Shower Floors</h2>
    <h3 class="abs heading heading--section importance-heading">Importance Of Showering Floor</h3>
    <p class="abs body-copy importance-copy">With a seamless design with no no surface joints there's less to clean because there are fewer areas where mildew and grime can gather which is very unpleasant to clean up.</p>
    <h3 class="abs heading heading--section products-heading">Our Products</h3>
    <p class="abs body-copy products-copy">Lorem Ipsum is simply dummy text of the printing and typesetting industry. Lorem Ipsum has been the industry's standard dummy text ever since the 1500s, when an unknown printer took a galley of type and scrambled it to make a type specimen book.</p>
    <div class="abs back-brand">
      <span class="brand-mark" style="width:12px;height:12px"></span>
      <div class="brand-name">Northridge Slabworks</div>
      <div class="brand-sub">Stainless Stone</div>
    </div>
  </div>
</section>

</body>
</html>
```